FAST TURN AROUND - Yoga & Sound Meditation Event Flyer

Our organization - Tarrow Guidance Alliance - is currently looking for someone to create a flyer for an upcoming Yoga & Sound Meditation Event.

We are looking for the following deliverables:
Versions of the Flyer created for Social Media (Long Story & Square Post) that includes the following information. (Not including the categories)
Event Title: Tarrow Flow & Hum Unwind Session - Bayline Mix
Event Date & Time: Wednesday, April 20 | 7P - 9P
Event Location: Reedhall at Cobbleyard
Tarrow Logo: (Both black and white versions are attached. Feel free to use whichever makes more sense based on the lighting)

We would want a version of this for the eight different background images provided. For the test, you can submit 1-2 since the rest of the details will be the same once we chose the information design.

```html
<!DOCTYPE html>
<html lang="en">
<head>
<meta charset="utf-8">
<title>Tarrow Flow &amp; Hum – Event Flyers</title>
<link href="https://fonts.googleapis.com/css2?family=Federo&family=Open+Sans:wght@400;800&family=Playfair+Display:wght@400&display=swap" rel="stylesheet">
<style>
  :root{
    --board:#b1b3d2;
    --ink:#050506;
    --white:#ffffff;
    --info-bg:#8e8fb8;
    --green:#21b14b;
    --yellow:#f4e51c;
    --orange:#f7931e;
    --red:#ed1c3a;
    --magenta:#e6177f;
    --purple:#7a3f98;
    --blue:#2e4aa8;
    --rainbow:linear-gradient(90deg,var(--green),var(--yellow) 28%,var(--orange) 45%,var(--red) 60%,var(--magenta) 75%,var(--purple) 90%,var(--blue));
  }
  *{margin:0;padding:0;box-sizing:border-box}
  html,body{width:1200px;height:1200px;overflow:hidden;background:var(--board)}
  .board{position:relative;width:1200px;height:1200px}
  .flyer{position:absolute;background:var(--ink);overflow:hidden;color:var(--white)}
  .flyer--story{left:67px;top:173px;width:505px;height:897px}
  .flyer--square{left:628px;top:370px;width:506px;height:506px}

  .brand{position:absolute;left:0;right:0;text-align:center}
  .brand__name{display:block;font-family:"Open Sans",sans-serif;font-weight:800;letter-spacing:.5px;line-height:1}
  .brand__sub{display:block;font-family:"Open Sans",sans-serif;font-weight:400;line-height:1.2}

  .title-frame{position:absolute}
  .title-frame svg{position:absolute;inset:0;width:100%;height:100%}
  .title{position:absolute;left:0;right:0;text-align:center;font-family:"Federo",sans-serif;line-height:1}
  .title span{background:var(--rainbow);-webkit-background-clip:text;background-clip:text;color:transparent;white-space:nowrap}

  .info{position:absolute;background:var(--info-bg);text-align:center;font-family:"Playfair Display",serif;color:var(--white);line-height:1.2}
  .pin{display:inline-block;vertical-align:-2px;margin-right:6px}

  .photo-bg{position:absolute;background:radial-gradient(ellipse at 72% 45%,#2b2b2b 0%,#1c1c1c 35%,#0a0a0a 75%)}
  .tile{position:absolute}
  .tile--gong{background:linear-gradient(135deg,#e8e4dc,#b59a7a 55%,#6b4a2c)}
  .tile--prayer{background:linear-gradient(160deg,#9a9a94,#3a2a26 55%,#1a1210)}
  .tile--candle{background:radial-gradient(circle at 55% 40%,#e07a24,#6a2c0c 50%,#1c0c06)}
  .tile--rest{background:linear-gradient(180deg,#d8d2cc,#8d8aa6 55%,#5c587a)}
  .tile--grey{background:linear-gradient(160deg,#555,#2e2e2e)}
  .tile--dark{background:#101010}

  .rainbow-bar{position:absolute;left:0;right:0;bottom:0;background:var(--rainbow)}
</style>
</head>
<body>
<svg width="0" height="0" style="position:absolute">
  <defs>
    <linearGradient id="frameGrad" x1="0" y1="0" x2="1" y2="0">
      <stop offset="0" stop-color="#21b14b"/>
      <stop offset=".3" stop-color="#f4e51c"/>
      <stop offset=".5" stop-color="#ed1c3a"/>
      <stop offset=".75" stop-color="#e6177f"/>
      <stop offset=".9" stop-color="#7a3f98"/>
      <stop offset="1" stop-color="#2e4aa8"/>
    </linearGradient>
  </defs>
</svg>

<main class="board">

  <!-- Story format -->
  <section class="flyer flyer--story">
    <div class="photo-bg" style="left:0;top:380px;width:505px;height:500px" role="img" aria-label="Black and white photo of a woman in profile seated in meditation"></div>
    <div class="tile tile--gong" style="left:0;top:430px;width:150px;height:150px" role="img" aria-label="Photo of a man playing a gong"></div>
    <div class="tile tile--grey" style="left:0;top:580px;width:150px;height:150px" role="img" aria-label="Greyscale photo of yoga mats"></div>
    <div class="tile tile--prayer" style="left:150px;top:580px;width:151px;height:150px" role="img" aria-label="Photo of a woman with hands in prayer position"></div>
    <div class="tile tile--candle" style="left:0;top:730px;width:150px;height:150px" role="img" aria-label="Photo of a candlelit sound bath room"></div>
    <div class="tile tile--grey" style="left:150px;top:730px;width:151px;height:150px" role="img" aria-label="Greyscale photo of a hand resting on a blanket"></div>
    <div class="tile tile--rest" style="left:301px;top:730px;width:150px;height:150px" role="img" aria-label="Photo of a person resting under a blanket on a mat"></div>

    <div class="brand" style="top:46px">
      <span class="brand__name" style="font-size:44px">tarrow.</span>
      <span class="brand__sub" style="font-size:14px;margin-top:3px">Tarrow Guidance Alliance</span>
    </div>

    <div class="title-frame" style="left:42px;top:136px;width:421px;height:189px">
      <svg viewBox="0 0 421 189" preserveAspectRatio="none"><rect x="1" y="1" width="419" height="187" fill="none" stroke="url(#frameGrad)" stroke-width="2"/></svg>
      <div class="title" style="top:17px;font-size:33px"><span>Tarrow Flow &amp; Hum</span></div>
      <div class="title" style="top:55px;font-size:35px"><span>Unwind Session</span></div>
      <div class="title" style="top:97px;font-size:33px"><span>- Bayline Mix -</span></div>
    </div>

    <div class="info" style="left:107px;top:282px;width:291px;height:111px;padding-top:11px;font-size:21px">
      <div>Wednesday, April 20</div>
      <div>7P – 9P</div>
      <div style="margin-top:6px"><svg class="pin" width="13" height="18" viewBox="0 0 12 17"><path d="M6 0a6 6 0 0 0-6 6c0 4.5 6 11 6 11s6-6.5 6-11a6 6 0 0 0-6-6zm0 8.5A2.5 2.5 0 1 1 6 3.5a2.5 2.5 0 0 1 0 5z" fill="#fff"/></svg>Reedhall at Cobbleyard</div>
    </div>

    <div class="rainbow-bar" style="height:17px"></div>
  </section>

  <!-- Square format -->
  <section class="flyer flyer--square">
    <div class="photo-bg" style="left:0;top:230px;width:506px;height:267px" role="img" aria-label="Black and white photo of a woman in profile seated in meditation"></div>
    <div class="tile tile--gong" style="left:0;top:280px;width:108px;height:109px" role="img" aria-label="Photo of a man playing a gong"></div>
    <div class="tile tile--prayer" style="left:216px;top:280px;width:108px;height:109px" role="img" aria-label="Photo of a woman with hands in prayer position"></div>
    <div class="tile tile--dark" style="left:0;top:389px;width:108px;height:108px"></div>
    <div class="tile tile--rest" style="left:108px;top:389px;width:108px;height:108px" role="img" aria-label="Photo of a person resting under a blanket on a mat"></div>
    <div class="tile tile--grey" style="left:216px;top:389px;width:108px;height:108px" role="img" aria-label="Greyscale photo of yoga mats"></div>
    <div class="tile tile--candle" style="left:324px;top:389px;width:108px;height:108px" role="img" aria-label="Photo of a candlelit sound bath room"></div>

    <div class="brand" style="top:18px">
      <span class="brand__name" style="font-size:33px">tarrow.</span>
      <span class="brand__sub" style="font-size:11px;margin-top:2px">Tarrow Guidance Alliance</span>
    </div>

    <div class="title-frame" style="left:42px;top:74px;width:423px;height:132px">
      <svg viewBox="0 0 423 132" preserveAspectRatio="none"><rect x="1" y="1" width="421" height="130" fill="none" stroke="url(#frameGrad)" stroke-width="2"/></svg>
      <div class="title" style="top:10px;font-size:28px"><span>Tarrow Flow &amp; Hum</span></div>
      <div class="title" style="top:42px;font-size:35px"><span>Unwind Session</span></div>
      <div class="title" style="top:85px;font-size:23px;letter-spacing:3px"><span>- Bayline Mix -</span></div>
    </div>

    <div class="info" style="left:107px;top:188px;width:292px;height:63px;padding-top:7px;font-size:17px">
      <div>Wednesday, April 20 &nbsp;|&nbsp; 7P – 9P</div>
      <div style="margin-top:6px"><svg class="pin" width="11" height="15" viewBox="0 0 12 17"><path d="M6 0a6 6 0 0 0-6 6c0 4.5 6 11 6 11s6-6.5 6-11a6 6 0 0 0-6-6zm0 8.5A2.5 2.5 0 1 1 6 3.5a2.5 2.5 0 0 1 0 5z" fill="#fff"/></svg>Reedhall at Cobbleyard</div>
    </div>

    <div class="rainbow-bar" style="height:9px"></div>
  </section>

</main>
</body>
</html>
```